Flickora Channel Design

Create the design and layout for a new feature we are implementing in Flickora called channels. These channels will be for example: 48317, Keeper of the Ashes, Court of Falcons, and etc. These channels will allow people to join the channel and discuss freely about the channel specifically.

Flickora is the app, it is free to download. Download the app and go to messaging and this is where the channels are going to lay. We need what the screen is going to look like within our color scheme, but also once you join the channel how are the messages going to look. I sent a few examples below of what ScreenLog uses and Chatterly Uses. I want ours to look way better. I would like to see designs for our new feature we are looking to launch with channels for movies and shows. Users can join these channels and join in on the conversation.

Industry/Entity Type

Moves and Shows

Requirements
Nice to have
• Follow my color scheme that is already in place on Flickora app. Download Flickora on the app store.

```html
<!DOCTYPE html>
<html lang="en">
<head>
<meta charset="utf-8">
<title>Flickora – Channels App Design</title>
<link rel="stylesheet" href="https://fonts.googleapis.com/css2?family=Poppins:wght@400;500;600;700&family=Montserrat:wght@600&display=swap">
<style>
  :root{
    --peach:#fdd9c9;
    --paper:#ffffff;
    --orange:#ff5a1f;
    --blue:#1f7fad;
    --ink:#1d2733;
    --muted:#8a9099;
    --line:#e8eaee;
    --seg:#eceef1;
    --highlight:#fdf1ea;
    --chat-bg:#e3f6fa;
    --cyan-soft:#dff6fb;
  }
  *{box-sizing:border-box;margin:0;padding:0}
  html,body{width:1200px;height:1200px;overflow:hidden}
  body{background:var(--peach);font-family:"Poppins",sans-serif;color:var(--ink);position:relative}
  ul{list-style:none}
  .sheet{position:absolute;left:17px;top:17px;width:1166px;height:1166px;background:var(--paper);border-radius:30px}

  /* brand block */
  .brand{position:absolute;left:135px;top:160px;width:160px;text-align:center}
  .brand-mark{width:155px;height:123px;margin:0 auto 20px;border-radius:24px;background:linear-gradient(180deg,#ffffff,var(--cyan-soft))}
  .brand-name{font-weight:700;font-size:38px;color:var(--blue);letter-spacing:-0.5px;line-height:1}
  .brand-tag{display:block;margin:16px auto 0;border:2px solid var(--orange);color:var(--orange);font-family:"Montserrat",sans-serif;font-weight:600;font-size:12px;letter-spacing:5px;line-height:20px;padding:2px 0 2px 5px;width:158px;white-space:nowrap;text-align:center}

  /* screen captions */
  .caption{position:absolute;top:614px;width:260px;text-align:center;font-family:"Montserrat",sans-serif;font-weight:600;font-size:9px;line-height:12px;letter-spacing:4.2px;color:var(--blue)}

  /* screens */
  .screen{position:absolute;top:657px;width:211px;height:452px;border-radius:26px;background:#fff;border:1px solid var(--line);overflow:hidden;box-shadow:0 6px 18px rgba(29,39,51,.08)}
  .status{position:absolute;top:12px;left:0;right:0;height:12px}
  .status .time{position:absolute;left:27px;font-weight:600;font-size:9px;line-height:12px}
  .status svg{position:absolute;right:22px;top:2px}
  .menu{position:absolute;left:12px;top:38px}
  .segment{position:absolute;left:36px;top:34px;width:134px;height:19px;background:var(--seg);border-radius:6px;display:flex;padding:2px;font-size:6px;font-weight:500}
  .segment span{flex:1;display:flex;align-items:center;justify-content:center;border-radius:4px}
  .segment .on{background:#fff;color:var(--orange)}

  .channels-row{position:absolute;top:68px;left:0;right:0;height:34px;border-bottom:1px solid var(--line);background:linear-gradient(180deg,#fff,#f5fbfd)}
  .chan{position:absolute;top:0;width:26px;height:26px;border-radius:50%}
  .chan.active::after{content:"";position:absolute;left:1px;right:1px;bottom:-6px;height:2px;border-radius:2px;background:var(--orange)}
  .chan-add{position:absolute;left:146px;top:0;width:26px;height:26px;border-radius:50%;background:#fff;box-shadow:0 1px 4px rgba(0,0,0,.12);color:var(--blue);font-size:16px;line-height:25px;text-align:center}

  .channel-title{position:absolute;left:11px;top:111px;font-weight:700;font-size:10px}
  .kebab{position:absolute;right:12px;top:113px}
  .cover{position:absolute;left:11px;top:135px;width:189px;height:105px;border-radius:6px;background:linear-gradient(180deg,#7d8a96 0%,#4b5662 45%,#2a323b 100%)}

  .search{position:absolute;height:18px;border:1px solid var(--line);border-radius:10px;font-size:6px;color:#b4b8be;display:flex;align-items:center;padding-left:9px;gap:5px}
  .invite{position:absolute;left:151px;top:253px;width:48px;height:18px;border-radius:10px;background:var(--blue);color:#fff;font-size:6px;font-weight:600;display:flex;align-items:center;justify-content:center;gap:3px}

  .section{position:absolute;left:11px;font-size:7.5px;font-weight:600}
  .row-link{position:absolute;left:11px;right:12px;height:12px;display:flex;align-items:center;font-size:6px;font-weight:500;gap:6px}
  .row-link .chev{margin-left:auto;color:var(--orange);font-size:8px}
  .row-link .hash{color:var(--blue);font-weight:700;font-size:8px;width:8px}

  .tabbar{position:absolute;left:0;right:0;top:406px;height:46px;border-top:1px solid var(--line);background:#fff}
  .tabbar .icons{position:absolute;left:14px;right:14px;top:7px;display:flex;justify-content:space-between}
  .tabbar .active-line{position:absolute;top:-1px;width:14px;height:2px;background:var(--orange);border-radius:2px}
  .home-bar{position:absolute;left:64px;width:80px;height:2.5px;bottom:9px;border-radius:2px;background:var(--ink)}

  /* messages */
  .page-title{position:absolute;left:11px;top:70px;font-size:10px;font-weight:700}
  .threads{position:absolute;left:4px;right:4px;top:113px}
  .thread{position:relative;height:31.4px;display:flex;align-items:center;padding:0 6px 0 7px;border-radius:6px}
  .thread.hl{background:var(--highlight)}
  .avatar{width:23px;height:23px;border-radius:50%;flex:none}
  .thread .body{margin-left:6px;flex:1;min-width:0;padding-right:30px}
  .thread .name{font-size:6px;font-weight:500;line-height:8px}
  .thread .name.unread{font-weight:600}
  .thread .text{font-size:4.8px;color:var(--muted);white-space:nowrap;overflow:hidden;text-overflow:ellipsis;line-height:7px}
  .thread .text.unread{color:var(--ink)}
  .thread .meta{position:absolute;right:6px;top:7px;text-align:right;font-size:5px;color:var(--muted)}
  .thread .meta.unread{color:var(--ink);font-weight:600}
  .dot{display:block;width:4px;height:4px;border-radius:50%;background:var(--orange);margin:3px 0 0 auto}
  .fab{position:absolute;left:173px;top:371px;width:26px;height:26px;border-radius:50%;background:var(--orange);box-shadow:0 3px 8px rgba(255,90,31,.35);display:flex;align-items:center;justify-content:center}

  /* chat */
  .chat{background:linear-gradient(180deg,#fff 12%,var(--chat-bg) 100%)}
  .chat-head{position:absolute;left:12px;right:12px;top:34px;height:24px;display:flex;align-items:center;gap:6px}
  .chat-head .avatar{width:20px;height:20px}
  .chat-head .who{font-size:8px;font-weight:600;line-height:9px}
  .chat-head .status-line{font-size:5px;color:var(--muted);display:flex;align-items:center;gap:2px}
  .chat-head .status-line i{width:4px;height:4px;border-radius:50%;background:#2fbf5a;display:block}
  .chat-head .kebab2{margin-left:auto}
  .stamp{position:absolute;top:63px;left:0;right:0;text-align:center;font-size:5px;color:var(--muted)}
  .thread-area{position:absolute;left:12px;right:12px;top:83px}
  .msg{font-size:6.4px;line-height:11px;padding:4px 7px;border-radius:7px;max-width:134px}
  .msg.out{background:var(--blue);color:#fff;margin-left:auto;text-align:center}
  .msg.in{background:#fff;border:1px solid var(--line)}
  .grp-in{display:flex;gap:5px;align-items:flex-start}
  .grp-in .avatar{width:17px;height:17px;margin-top:1px}
  .grp-in .stack{display:flex;flex-direction:column;gap:3px}
  .reply-bar{position:absolute;left:0;right:0;top:404px;height:48px;background:#fff;border-top:1px solid var(--line)}
  .reply-input{position:absolute;left:30px;top:7px;width:146px;height:20px;border:1px solid var(--line);border-radius:11px;font-size:6px;color:#b4b8be;padding-left:8px;line-height:18px}
  .send{position:absolute;left:183px;top:9px;width:16px;height:16px;border-radius:50%;background:var(--orange);display:flex;align-items:center;justify-content:center}
  .plus{position:absolute;left:11px;top:11px}
</style>
</head>
<body>
<svg width="0" height="0" style="position:absolute" aria-hidden="true">
  <defs>
    <symbol id="i-home" viewBox="0 0 12 12"><path d="M1.5 6 6 2l4.5 4v4.5h-3V8h-3v2.5h-3z" fill="#1f7fad"/></symbol>
    <symbol id="i-hash" viewBox="0 0 12 12"><circle cx="6" cy="6" r="5" fill="#ff5a1f"/><path d="M4.6 3.5 4 8.5M7.6 3.5 7 8.5M3.3 5h5.4M3 7h5.4" stroke="#fff" stroke-width=".9"/></symbol>
    <symbol id="i-search" viewBox="0 0 12 12"><circle cx="5.2" cy="5.2" r="3.8" fill="#1f7fad"/><path d="m8 8 2.7 2.7" stroke="#1f7fad" stroke-width="1.4" stroke-linecap="round"/></symbol>
    <symbol id="i-clap" viewBox="0 0 12 12"><rect x="1.5" y="4" width="9" height="6.5" rx="1" fill="#1f7fad"/><path d="M1.5 2.2 10 1l.3 2-8.5 1.2z" fill="#1f7fad"/><path d="m5 5.8 2.5 1.5L5 8.8z" fill="#fff"/></symbol>
    <symbol id="i-wand" viewBox="0 0 12 12"><path d="m2 10.5 6.5-6.5" stroke="#1f7fad" stroke-width="1.6" stroke-linecap="round"/><path d="M9 1v2M8 2h2M10.5 5v1.6M9.7 5.8h1.6M5 1.5v1.4M4.3 2.2h1.4" stroke="#1f7fad" stroke-width=".9"/></symbol>
    <symbol id="i-status" viewBox="0 0 34 8"><rect x="0" y="5" width="1.6" height="3" fill="#1d2733"/><rect x="2.6" y="3.5" width="1.6" height="4.5" fill="#1d2733"/><rect x="5.2" y="2" width="1.6" height="6" fill="#1d2733"/><rect x="7.8" y="0.5" width="1.6" height="7.5" fill="#1d2733"/><path d="M12.5 3.2a5 5 0 0 1 7 0M14 4.8a3 3 0 0 1 4 0" stroke="#1d2733" stroke-width="1.1" fill="none"/><circle cx="16" cy="6.6" r=".9" fill="#1d2733"/><rect x="22" y="1" width="11" height="6" rx="1.6" fill="#1d2733"/></symbol>
    <symbol id="i-menu" viewBox="0 0 10 8"><path d="M0 1h10M0 4h10M0 7h10" stroke="#1f7fad" stroke-width="1"/></symbol>
    <symbol id="i-kebab" viewBox="0 0 3 9"><circle cx="1.5" cy="1" r=".9" fill="#1d2733"/><circle cx="1.5" cy="4.5" r=".9" fill="#1d2733"/><circle cx="1.5" cy="8" r=".9" fill="#1d2733"/></symbol>
    <symbol id="i-mag" viewBox="0 0 8 8"><circle cx="3.3" cy="3.3" r="2.4" fill="none" stroke="#8a9099" stroke-width="1"/><path d="m5.2 5.2 2 2" stroke="#8a9099" stroke-width="1"/></symbol>
  </defs>
</svg>

<main class="sheet">
  <section class="brand">
    <div class="brand-mark"></div>
    <div class="brand-name">Flickora</div>
    <div class="brand-tag">APP DESIGN</div>
  </section>

  <h2 class="caption" style="left:166px">CHANNELS SCREEN</h2>
  <h2 class="caption" style="left:441px">MESSAGES SCREEN</h2>
  <h2 class="caption" style="left:714px">VIEW/REPLY MESSAGE</h2>
</main>

<!-- Channels screen -->
<article class="screen" style="left:208px">
  <div class="status"><span class="time">9:41</span><svg width="34" height="8"><use href="#i-status"/></svg></div>
  <svg class="menu" width="10" height="8"><use href="#i-menu"/></svg>
  <div class="segment"><span class="on">Channels</span><span>Messages</span></div>

  <div class="channels-row">
    <div class="chan" style="left:10px;background:radial-gradient(circle,#c8321e,#1b1b1b 70%)" role="img" aria-label="Channel poster avatar"></div>
    <div class="chan active" style="left:44px;background:linear-gradient(160deg,#e2c93a,#3a3f4a)" role="img" aria-label="Harbor Precinct 12 poster avatar"></div>
    <div class="chan" style="left:77px;background:linear-gradient(160deg,#b2453a,#3b3a6a)" role="img" aria-label="Channel poster avatar"></div>
    <div class="chan" style="left:111px;background:linear-gradient(180deg,#d6c7a6,#6f7378)" role="img" aria-label="Channel poster avatar"></div>
    <div class="chan-add">+</div>
  </div>

  <h3 class="channel-title">Harbor Precinct 12</h3>
  <svg class="kebab" width="3" height="9"><use href="#i-kebab"/></svg>
  <div class="cover" role="img" aria-label="Cast of Harbor Precinct 12 walking across a bridge"></div>

  <div class="search" style="left:11px;top:253px;width:135px"><svg width="7" height="7"><use href="#i-mag"/></svg>Search</div>
  <div class="invite">
    <svg width="8" height="7" viewBox="0 0 8 7"><circle cx="4.5" cy="2" r="1.6" fill="#fff"/><path d="M1.8 7a2.7 2.4 0 0 1 5.4 0z" fill="#fff"/><path d="M0 3h2.4M1.2 1.8v2.4" stroke="#fff" stroke-width=".8"/></svg>Invite
  </div>

  <div class="section" style="top:287px">Information</div>
  <div class="row-link" style="top:304px"><svg width="8" height="7" viewBox="0 0 8 7"><path d="M4 0 8 7H0z" fill="#1f7fad"/><rect x="3.6" y="2.4" width=".8" height="2.4" fill="#fff"/></svg>channel-rules<span class="chev">›</span></div>
  <div class="row-link" style="top:325px"><svg width="8" height="8" viewBox="0 0 8 8"><circle cx="4" cy="4" r="3.6" fill="#1f7fad"/><rect x="3.6" y="1.8" width=".8" height="2.6" fill="#fff"/><circle cx="4" cy="5.8" r=".5" fill="#fff"/></svg>news-and-events<span class="chev">›</span></div>

  <div class="section" style="top:360px">Community</div>
  <div class="row-link" style="top:376px"><span class="hash">#</span>introduce-yourself<span class="chev">›</span></div>
  <div class="row-link" style="top:394px"><span class="hash">#</span>news-and-events<span class="chev">›</span></div>

  <nav class="tabbar">
    <span class="active-line" style="left:54px"></span>
    <div class="icons">
      <svg width="12" height="12"><use href="#i-home"/></svg>
      <svg width="12" height="12"><use href="#i-hash"/></svg>
      <svg width="12" height="12"><use href="#i-search"/></svg>
      <svg width="12" height="12"><use href="#i-clap"/></svg>
      <svg width="12" height="12"><use href="#i-wand"/></svg>
    </div>
    <span class="home-bar"></span>
  </nav>
</article>

<!-- Messages screen -->
<article class="screen" style="left:483px">
  <div class="status"><span class="time">9:41</span><svg width="34" height="8"><use href="#i-status"/></svg></div>
  <svg class="menu" width="10" height="8"><use href="#i-menu"/></svg>
  <div class="segment"><span>Channels</span><span class="on">Messages</span></div>

  <h3 class="page-title">Messages</h3>
  <div class="search" style="left:11px;top:90px;width:189px"><svg width="7" height="7"><use href="#i-mag"/></svg>Search</div>

  <ul class="threads">
    <li class="thread"><span class="avatar" style="background:#c7c9cc" role="img" aria-label="MiraLoopfield profile photo"></span><div class="body"><div class="name unread">MiraLoopfield</div><div class="text unread">That was awesome!</div></div><div class="meta unread">2m ago<span class="dot"></span></div></li>
    <li class="thread"><span class="avatar" style="background:#9a9c9f" role="img" aria-label="Orin1984 profile photo"></span><div class="body"><div class="name">Orin1984</div><div class="text">I definitely like it. HBU?</div></div><div class="meta">10:16 AM</div></li>
    <li class="thread hl"><span class="avatar" style="background:#c99a7c" role="img" aria-label="quiet.ink.writer profile photo"></span><div class="body"><div class="name unread">quiet.ink.writer</div><div class="text unread">I think I've seen this film before and I didn't like the end…</div></div><div class="meta unread">12:13 PM<span class="dot"></span></div></li>
    <li class="thread"><span class="avatar" style="background:#5f8c8a" role="img" aria-label="thatquietviewer profile photo"></span><div class="body"><div class="name">thatquietviewer</div><div class="text">No problem</div></div><div class="meta">Yesterday</div></li>
    <li class="thread"><span class="avatar" style="background:#caa27a" role="img" aria-label="Lenora_pk profile photo"></span><div class="body"><div class="name">Lenora_pk</div><div class="text">Agree! totally one of my favorite movies of all time</div></div><div class="meta">Yesterday</div></li>
    <li class="thread"><span class="avatar" style="background:#6e5a4c" role="img" aria-label="Dario.calm profile photo"></span><div class="body"><div class="name unread">Dario.calm</div><div class="text unread">Wow</div></div><div class="meta unread">Aug 8<span class="dot"></span></div></li>
    <li class="thread"><span class="avatar" style="background:#5c5f66" role="img" aria-label="tobin.vale profile photo"></span><div class="body"><div class="name">tobin.vale</div><div class="text">the visual effects are so impressive not gonna lie</div></div><div class="meta">Aug 8</div></li>
    <li class="thread"><span class="avatar" style="background:#8a7664" role="img" aria-label="Prue_0822 profile photo"></span><div class="body"><div class="name unread">Prue_0822</div><div class="text unread">No problem</div></div><div class="meta unread">Aug 7<span class="dot"></span></div></li>
    <li class="thread"><span class="avatar" style="background:#3e3a38" role="img" aria-label="nookofK profile photo"></span><div class="body"><div class="name">nookofK</div><div class="text">they are fantastic!</div></div></li>
  </ul>

  <div class="fab"><svg width="12" height="12" viewBox="0 0 12 12"><circle cx="6" cy="6" r="4.6" fill="none" stroke="#fff" stroke-width="1.2"/><path d="m4.2 7.8 3.6-3.6" stroke="#fff" stroke-width="1.4" stroke-linecap="round"/></svg></div>

  <nav class="tabbar">
    <span class="active-line" style="left:54px"></span>
    <div class="icons">
      <svg width="12" height="12"><use href="#i-home"/></svg>
      <svg width="12" height="12"><use href="#i-hash"/></svg>
      <svg width="12" height="12"><use href="#i-search"/></svg>
      <svg width="12" height="12"><use href="#i-clap"/></svg>
      <svg width="12" height="12"><use href="#i-wand"/></svg>
    </div>
    <span class="home-bar"></span>
  </nav>
</article>

<!-- View / reply screen -->
<article class="screen chat" style="left:756px">
  <div class="status"><span class="time">9:41</span><svg width="34" height="8"><use href="#i-status"/></svg></div>
  <header class="chat-head">
    <svg width="9" height="8" viewBox="0 0 9 8"><path d="M8.5 4H1M4 1 1 4l3 3" stroke="#1f7fad" stroke-width="1" fill="none"/></svg>
    <span class="avatar" style="background:#c99a7c" role="img" aria-label="quiet.ink.writer profile photo"></span>
    <div><div class="who">quiet.ink.writer</div><div class="status-line"><i></i>Online now</div></div>
    <svg class="kebab2" width="3" height="9"><use href="#i-kebab"/></svg>
  </header>
  <div class="stamp">12:13 PM</div>

  <div class="thread-area">
    <p class="msg out" style="margin-bottom:14px;width:max-content">Do you think this is the best movie?</p>
    <div class="grp-in" style="margin-bottom:8px">
      <span class="avatar" style="background:#c99a7c" role="img" aria-label="quiet.ink.writer profile photo"></span>
      <div class="stack">
        <p class="msg in" style="align-self:flex-start">It's really a great movie…</p>
        <p class="msg in">Honestly, that final twist still keeps me up at night…</p>
      </div>
    </div>
    <p class="msg out" style="margin-bottom:3px;width:max-content">That's a line from your review 😂</p>
    <p class="msg out" style="margin-bottom:8px">By the way, have you watched the Season 3 finale of the show "ECHO"?</p>
    <div class="grp-in" style="margin-bottom:8px">
      <span class="avatar" style="background:#c99a7c" role="img" aria-label="quiet.ink.writer profile photo"></span>
      <div class="stack"><p class="msg in">I think I've seen this film before and I didn't like the ending</p></div>
    </div>
    <p class="msg out" style="margin-bottom:3px">That's exactly the score played in the background during the finale.</p>
    <p class="msg out" style="width:max-content">Wait…that's your playlist, right?</p>
  </div>

  <footer class="reply-bar">
    <svg class="plus" width="10" height="10" viewBox="0 0 10 10"><circle cx="5" cy="5" r="4.5" fill="#1f7fad"/><path d="M5 2.8v4.4M2.8 5h4.4" stroke="#fff" stroke-width="1"/></svg>
    <div class="reply-input">Reply…</div>
    <div class="send"><svg width="8" height="8" viewBox="0 0 8 8"><path d="M1 1 7.5 4 1 7l1-3z" fill="#fff"/></svg></div>
    <span class="home-bar"></span>
  </footer>
</article>
</body>
</html>
```